Advertisement insert for magazine

Create a 5 X 4.75 advertisement for a magazine. Design must catch the eye of the reader and properly represent our brand. This will be in LANTERN magazine a local affluent magazine.

The goal of this advertisement is to represent a progressive firm with an amazing portfolio.

Target Market(s)

local businesses and business leaders of Florida.

Industry/Entity Type

Architecture

Font styles to use
Other font styles liked:
• Calibri, Calibri light

Requirements
Must have
• Modern Progressive Design. Our logo, our address and telephone number and our project images we have attached.
Should not have
• I have attached the ad from last year, we DO NOT want to replicate this ad, however this should give you an idea of the size and overall goal of the advertisement.
• (SEE LANTERN MAGAZINE KTW PDF)

```html
<!DOCTYPE html>
<html lang="en">
<head>
<meta charset="utf-8">
<title>Harrow Vance + Partners — Magazine Advertisement</title>
<link rel="stylesheet" href="https://fonts.googleapis.com/css2?family=Jost:wght@300;400&family=Roboto+Condensed:wght@400&display=swap">
<style>
  :root {
    --backdrop: #c9c9c9;
    --paper: #ffffff;
    --brand-blue: #0a73c4;
    --brand-orange: #f07a30;
    --panel-grey: #9d9ea1;
    --ink: #1d1d1f;
    --rule: #1d1d1f;
    --label-white: #ffffff;
  }
  html, body {
    margin: 0;
    width: 1200px;
    height: 1200px;
    overflow: hidden;
    background: var(--backdrop);
  }
  .ad-page {
    position: absolute;
    left: 30px;
    top: 88px;
    width: 1140px;
    height: 1024px;
    background: var(--paper);
  }
  .ad-page svg { display: block; width: 100%; height: 100%; }
  .section-label {
    font-family: "Jost", sans-serif;
    font-weight: 300;
    font-size: 24px;
    letter-spacing: 5px;
    fill: var(--label-white);
  }
  .brand-name {
    font-family: "Roboto Condensed", sans-serif;
    font-weight: 400;
    fill: var(--ink);
  }
  .brand-name--main { font-size: 40px; letter-spacing: 0.5px; }
  .brand-name--sub { font-size: 12px; letter-spacing: 7px; }
  .contact-line {
    font-family: "Roboto Condensed", sans-serif;
    font-weight: 400;
    font-size: 18px;
    fill: var(--ink);
  }
  .rule { stroke: var(--rule); stroke-width: 1.3; fill: none; }
</style>
</head>
<body>
<div class="ad-page">
<svg viewBox="0 0 1080 970" xmlns="http://www.w3.org/2000/svg">
  <defs>
    <linearGradient id="tone-lounge" x1="0" y1="0" x2="1" y2="1"><stop offset="0" stop-color="#e9eef2"/><stop offset=".55" stop-color="#3a5fa8"/><stop offset="1" stop-color="#b58f62"/></linearGradient>
    <linearGradient id="tone-showroom" x1="0" y1="0" x2="1" y2="1"><stop offset="0" stop-color="#f2c7c0"/><stop offset=".5" stop-color="#2f3f8f"/><stop offset="1" stop-color="#5b6b3a"/></linearGradient>
    <linearGradient id="tone-atrium" x1="0" y1="0" x2="1" y2="1"><stop offset="0" stop-color="#f4f4f2"/><stop offset="1" stop-color="#d8d2c8"/></linearGradient>
    <linearGradient id="tone-facade" x1="0" y1="0" x2="0" y2="1"><stop offset="0" stop-color="#8d95b8"/><stop offset=".6" stop-color="#6e6f7a"/><stop offset="1" stop-color="#3e6b3a"/></linearGradient>
    <linearGradient id="tone-villa" x1="0" y1="0" x2="0" y2="1"><stop offset="0" stop-color="#b69ac4"/><stop offset=".5" stop-color="#d8a77a"/><stop offset="1" stop-color="#5d4535"/></linearGradient>
    <linearGradient id="tone-dining" x1="0" y1="0" x2="0" y2="1"><stop offset="0" stop-color="#6f7870"/><stop offset=".6" stop-color="#9b6a43"/><stop offset="1" stop-color="#3a3d44"/></linearGradient>
    <linearGradient id="tone-storefront" x1="0" y1="0" x2="0" y2="1"><stop offset="0" stop-color="#5d8ecf"/><stop offset=".5" stop-color="#d7dbe0"/><stop offset="1" stop-color="#3c3a36"/></linearGradient>
    <linearGradient id="tone-waterview" x1="0" y1="0" x2="0" y2="1"><stop offset="0" stop-color="#e6ebee"/><stop offset=".5" stop-color="#6d8f6a"/><stop offset="1" stop-color="#7d7674"/></linearGradient>
    <linearGradient id="tone-condo" x1="0" y1="0" x2="0" y2="1"><stop offset="0" stop-color="#f4f2ef"/><stop offset=".6" stop-color="#c9cdd0"/><stop offset="1" stop-color="#4f7a3c"/></linearGradient>
  </defs>

  <!-- colour band -->
  <polygon class="accent-band" points="59,0 345,0 345,203 59,60" fill="var(--brand-blue)"/>

  <!-- project tiles -->
  <polygon role="img" aria-label="Photo of a bright lounge with a blue sofa opening onto a pool terrace" points="118,87 405,230.5 405,370.5 118,227" fill="url(#tone-lounge)"/>
  <polygon role="img" aria-label="Photo of a car showroom exterior at dusk with a clipped tree" points="350,54 637,197.5 637,333.5 350,190" fill="url(#tone-showroom)"/>
  <polygon role="img" aria-label="Photo of a white office atrium with a glass stair" points="643,202 928,344.5 928,484.5 643,342" fill="url(#tone-atrium)"/>
  <polygon role="img" aria-label="Photo of a modern building entrance with a green wall" points="415,232 700,374.5 700,515.5 415,373" fill="url(#tone-facade)"/>
  <polygon role="img" aria-label="Photo of a Mediterranean-style building with palm trees at sunset" points="0,337 277,475.5 277,620.5 0,482" fill="url(#tone-villa)"/>
  <polygon role="img" aria-label="Photo of a restaurant bar with wooden stools and patterned tile" points="285,480 573,624 573,768 285,624" fill="url(#tone-dining)"/>
  <polygon role="img" aria-label="Photo of a glazed storefront under a blue sky" points="493,430 780,573.5 780,717.5 493,574" fill="url(#tone-storefront)"/>
  <polygon role="img" aria-label="Photo of a lounge with a sectional sofa facing a waterway" points="788,582 1080,728 1080,873 788,727" fill="url(#tone-waterview)"/>
  <polygon role="img" aria-label="Photo of a white condominium building with bougainvillea" points="207,597 493,740 493,885 207,742" fill="url(#tone-condo)"/>

  <!-- service panels -->
  <g class="service-panel service-panel--architecture">
    <polygon points="200,285 487,428.5 487,565.5 200,422" fill="var(--panel-grey)"/>
    <text class="section-label" transform="translate(234,376) rotate(26.6)" textLength="232" lengthAdjust="spacing">ARCHITECTURE</text>
  </g>
  <g class="service-panel service-panel--interiors">
    <polygon points="708,387 996,531 996,674 708,530" fill="var(--brand-orange)"/>
    <text class="section-label" transform="translate(726,474) rotate(26.6)" textLength="262" lengthAdjust="spacing">INTERIOR DESIGN</text>
  </g>

  <!-- hairlines -->
  <line class="rule" x1="0" y1="172" x2="118" y2="231"/>
  <line class="rule" x1="118" y1="172" x2="118" y2="350"/>
  <line class="rule" x1="996" y1="224" x2="996" y2="530"/>
  <line class="rule" x1="928" y1="352" x2="1080" y2="428"/>
  <line class="rule" x1="573" y1="767" x2="830" y2="896"/>

  <!-- brand -->
  <g class="brand">
    <circle cx="670" cy="107" r="40" fill="var(--brand-blue)"/>
    <text class="brand-name brand-name--main" x="720" y="106">HARROW VANCE</text>
    <text class="brand-name brand-name--sub" x="822" y="124">+ PARTNERS</text>
  </g>

  <!-- contact -->
  <text class="contact-line" x="540" y="938" text-anchor="middle">418 Coral Avenue, West Palm Beach, Florida  |  (561) 555-0142  |  HarrowVance.com</text>
</svg>
</div>
</body>
</html>
```